Brightwell-Joinery - DL Flyer - Kitchen Renovations & Cabinetry - Eye Catching Design

Please design a creative, professional DL flyer for us (DL Size: 98 x 210mmm), incorporating details outlined below...

Font: Helvetica Neue (same as logo)

Front: Main logo (01.eps) as a feature, website on the bottom (brightwell-joinery.com.au).

Back: Three key words to be featured: Kitchens I Benchtops I Custom Cabinetry
2-3 clear images showing our work (more have been provided so you can select the images that work the best with the design). We have also attached the icon from our logo on 4 x different colour backgrounds, which could be incorporated (on back).
Text to include: 'Servicing all areas, we come to you!'

Contact details: 'Call us now on 0461 872 309'. enquiries@brightwell-joinery.com.au Lic. No. BLD 738402

Look forward to seeing what you come up with.

Target Market(s)

Home owners, 35-80+ age bracket

Industry/Entity Type

Kitchen

Font styles to use
Other font styles liked:
• Helvetica Neue

Requirements
Must have
• Logo and website on front page of flyer. Minimum of 2-3 images incorporated. Contact details as per project description. Text on back page, 3 key words: Kitchens I Benchtops I Custom Cabinetry
• Creative, eye-catching design layout. Consistent theming with business card (see attached), including colours (grey, white, blues)
Nice to have
• Creative, eye-catching way to incorporate photos.
Should not have
• Not too busy/cluttered

```html
<!DOCTYPE html>
<html lang="en">
<head>
<meta charset="utf-8">
<title>Brightwell-Joinery DL Flyer</title>
<link href="https://fonts.googleapis.com/css2?family=Arimo:wght@400;700&display=swap" rel="stylesheet">
<style>
:root{
  --page:#ededed;
  --paper:#ffffff;
  --edge:#d6d6d6;
  --tile-grey:#a7a7a7;
  --tile-text:#474747;
  --ink:#3d3d3d;
  --ink-soft:#7a7a7a;
  --brand-blue:#4a63a8;
  --contact-blue:#5c87c3;
  --areas-blue:#4e5fa3;
  --navy:#27305e;
  --call-light:#c9cfd8;
}
*{box-sizing:border-box;margin:0;padding:0}
html,body{width:1200px;height:1000px;overflow:hidden}
body{background:var(--page);font-family:"Arimo","Helvetica Neue",Arial,sans-serif;position:relative}
.panel{position:absolute;top:13px;width:456px;height:975px;background:var(--paper);border:1px solid var(--edge)}
.panel--front{left:130px}
.panel--back{left:615px}
.abs{position:absolute}

/* front */
.front-photo{left:23px;top:25px;width:408px;height:927px;border-radius:18px;
  background:linear-gradient(180deg,#ece3b0 0%,#e9de9c 22%,#e3d488 42%,#e8d98a 52%,#d6c57e 62%,#c7bb8c 72%,#9f9a86 84%,#7e7a6c 100%)}
.logo-tab{left:23px;top:25px;width:269px;height:77px;background:var(--paper);border-bottom-right-radius:20px}
.brand{left:36px;top:46px;display:flex;align-items:center;gap:8px}
.brand__mark{width:14px;height:14px;background:var(--brand-blue)}
.brand__name{font-size:20px;font-weight:700;color:var(--ink);letter-spacing:.2px;line-height:20px}
.brand__tagline{left:37px;top:68px;font-size:7.5px;letter-spacing:2.6px;color:var(--ink-soft)}
.area-band{left:23px;top:428px;width:327px;height:78px;background:var(--paper);border-radius:0 18px 18px 0;
  display:flex;align-items:center;padding-left:4px;font-size:14px;color:var(--ink);letter-spacing:.4px}
.web-tab{left:218px;top:896px;width:213px;height:56px;background:var(--paper);border-top-left-radius:18px;
  display:flex;align-items:center;padding-left:20px;font-size:14px;font-weight:700;color:var(--ink)}

/* back */
.tile{position:absolute}
.tile--photo{background:linear-gradient(135deg,#e6e4dc,#c9c6bb)}
.tile--word{background:var(--tile-grey);display:flex;align-items:center;justify-content:center;text-align:center;
  font-size:17px;font-weight:700;color:var(--tile-text);line-height:1.3}
.contact{background:var(--contact-blue);color:#fff}
.contact__icons{left:19px;top:38px;display:flex;align-items:center;gap:12px}
.call{font-size:17px;font-weight:400;color:var(--navy);margin-left:4px}
.call .us{color:#1b2147;font-weight:700}
.call .now{color:var(--call-light);font-weight:700}
.contact__lines{left:19px;top:92px;font-size:14px;line-height:17px}
.areas{background:var(--areas-blue);color:#fff;text-align:center;font-size:14px;font-weight:700;line-height:17px;padding-top:22px}
.areas .gap{height:17px}
.areas .light{font-weight:400}
.areas .dark{color:var(--navy)}
</style>
</head>
<body>

<section class="panel panel--front">
  <div class="abs front-photo" role="img" aria-label="Photo of a built-in home office with cream overhead cabinets, a long desk, computer, folders and two white chairs"></div>
  <div class="abs logo-tab"></div>
  <div class="abs brand"><span class="brand__mark"></span><span class="brand__name">BRIGHTWELL-JOINERY</span></div>
  <div class="abs brand__tagline">CABINETRY SOLUTIONS FOR YOUR HOME</div>
  <div class="abs area-band">SERVICING ALL AREAS, WE COME TO YOU</div>
  <div class="abs web-tab">brightwell-joinery.com.au</div>
</section>

<section class="panel panel--back">
  <div class="tile tile--word" style="left:24px;top:23px;width:157px;height:133px">KITCHENS</div>
  <div class="tile tile--photo" style="left:191px;top:23px;width:241px;height:133px;background:linear-gradient(160deg,#8c8a84 0%,#e9e7e1 30%,#dcd8cc 65%,#b9b49e 100%)" role="img" aria-label="Photo of a speckled stone kitchen benchtop with cooktop and cream cabinets"></div>
  <div class="tile tile--photo" style="left:24px;top:166px;width:408px;height:157px;background:linear-gradient(170deg,#cdd3c8 0%,#e6e8e2 35%,#f3f2ee 60%,#d8d4c8 100%)" role="img" aria-label="Photo of a white marble benchtop with sink, tap and glass splashback"></div>
  <div class="tile tile--photo" style="left:24px;top:333px;width:242px;height:132px;background:linear-gradient(160deg,#d9d5bd 0%,#cfcb9f 45%,#b9b78c 70%,#8a876f 100%)" role="img" aria-label="Photo of a built-in twin desk study nook with plant and chairs"></div>
  <div class="tile tile--word" style="left:276px;top:333px;width:156px;height:132px">BENCHTOPS</div>
  <div class="tile tile--photo" style="left:24px;top:476px;width:408px;height:157px;background:linear-gradient(90deg,#eeece6 0%,#e3e0d6 45%,#c9c2b2 68%,#e8e6e0 82%,#a07a4c 90%,#8d6a42 100%)" role="img" aria-label="Photo of white shaker kitchen drawers beside a wall oven and timber door"></div>
  <div class="tile tile--photo" style="left:24px;top:643px;width:130px;height:133px;background:linear-gradient(180deg,#4a5a7a 0%,#d9d6cf 35%,#e3e0d8 55%,#6b3f22 100%)" role="img" aria-label="Photo of a kitchen island with dark benchtop on a timber floor"></div>
  <div class="tile tile--word" style="left:164px;top:643px;width:130px;height:133px">CUSTOM<br>CABINETRY</div>
  <div class="tile tile--photo" style="left:303px;top:643px;width:129px;height:133px;background:linear-gradient(135deg,#2a2326,#4a3030 60%,#1c1a1c)" role="img" aria-label="Photo of dark floor-to-ceiling shelving with a library ladder"></div>

  <div class="tile contact" style="left:24px;top:785px;width:268px;height:165px">
    <div class="abs contact__icons">
      <svg width="32" height="32" viewBox="0 0 32 32" aria-hidden="true">
        <circle cx="16" cy="16" r="14.5" fill="none" stroke="#27305e" stroke-width="1.6"/>
        <path d="M11.5 9.5c1-.6 1.8-.4 2.3.5l1.1 2.2c.4.8.1 1.5-.6 2l-.8.5c.6 1.8 1.9 3.2 3.6 4l.6-.8c.5-.6 1.2-.8 2-.4l2.1 1.2c.8.5 1 1.3.4 2.2-.9 1.3-2.3 1.8-3.8 1.2-4-1.6-6.8-4.6-8-8.6-.4-1.6.1-3.1 1.1-4z" fill="#27305e"/>
      </svg>
      <svg width="34" height="30" viewBox="0 0 34 30" aria-hidden="true">
        <path d="M3 12 17 2 31 12V28H3Z" fill="none" stroke="#27305e" stroke-width="1.6" stroke-linejoin="round"/>
        <path d="M3 12 17 21 31 12M3 28 13 18M31 28 21 18" fill="none" stroke="#27305e" stroke-width="1.6"/>
      </svg>
      <span class="call">CALL<span class="us">US</span><span class="now">NOW</span></span>
    </div>
    <div class="abs contact__lines">0461 872 309<br>enquiries@brightwell-joinery.com.au<br>Lic. No. BLD 738402</div>
  </div>
  <div class="tile areas" style="left:302px;top:785px;width:130px;height:165px">
    SERVICING<br>ALL<br>AREAS
    <div class="gap"></div>
    <span class="light">WE</span><span class="dark">COME</span><br>TO<br>YOU
  </div>
</section>

</body>
</html>
```